Google slides for an upcoming presentation

I would like to recreate the jpeg to better match our company branding & color, as well as better resolution-- which is found in the PPTX. The slide should read....
"What are the biggest differences between Web 2.0 to Web 3.0"

Industry/Entity Type

Web3

Other font styles liked:
• Manrope

```html
<!DOCTYPE html>
<html lang="en">
<head>
<meta charset="UTF-8">
<title>Web 2.0 to Web 3.0</title>
<link rel="stylesheet" href="https://fonts.googleapis.com/css2?family=Manrope:wght@700;800&display=swap">
<style>
  :root {
    --navy-deep: #04285a;
    --navy: #0a3466;
    --glow: #2f6c93;
    --cyan: #4fd3f2;
    --white: #ffffff;
    --globe-pink: #e49cd2;
    --globe-blue: #9fc6ef;
    --server-blue: #3aa8ee;
    --server-violet: #6b1fa8;
  }
  * { margin: 0; padding: 0; box-sizing: border-box; }
  html, body { width: 1200px; height: 675px; overflow: hidden; background: var(--navy-deep); }
  .slide {
    position: relative;
    width: 1200px;
    height: 675px;
    overflow: hidden;
    background:
      radial-gradient(ellipse 420px 300px at 720px 520px, var(--glow) 0%, rgba(47,108,147,0.45) 45%, rgba(10,52,102,0) 100%),
      linear-gradient(180deg, var(--navy-deep) 0%, var(--navy) 100%);
    font-family: "Manrope", sans-serif;
    color: var(--white);
  }
  .globe-art {
    position: absolute;
    left: 44px;
    top: 124px;
    width: 370px;
    height: 370px;
    border-radius: 50%;
    background: radial-gradient(circle at 60% 55%, rgba(228,156,210,0.35) 0%, rgba(159,198,239,0.22) 55%, rgba(159,198,239,0.05) 100%);
  }
  .light-beam {
    position: absolute;
    left: 150px;
    top: 355px;
    width: 330px;
    height: 4px;
  }
  .server-art {
    position: absolute;
    left: 740px;
    top: 210px;
    width: 406px;
    height: 435px;
    background: linear-gradient(160deg, rgba(79,211,242,0.15) 0%, var(--server-blue) 40%, var(--server-violet) 100%);
    border-radius: 24px;
    opacity: 0.85;
    clip-path: polygon(35% 0, 100% 20%, 100% 80%, 55% 100%, 0 80%, 0 20%);
  }
  .title-block {
    position: absolute;
    left: 463px;
    top: 158px;
  }
  .kicker {
    font-weight: 800;
    font-size: 35px;
    line-height: 43px;
    letter-spacing: 0.2px;
  }
  .divider {
    width: 443px;
    height: 3px;
    background: var(--cyan);
    margin-top: 16px;
    margin-bottom: 12px;
  }
  .headline {
    font-weight: 800;
    font-size: 68px;
    line-height: 58px;
    letter-spacing: -1px;
  }
</style>
</head>
<body>
  <div class="slide">
    <div class="globe-art" role="img" aria-label="Wireframe globe of connected network nodes in pink and light blue"></div>
    <svg class="light-beam" viewBox="0 0 330 4" preserveAspectRatio="none" aria-hidden="true">
      <defs>
        <linearGradient id="beam" x1="0" x2="1" y1="0" y2="0">
          <stop offset="0" stop-color="#4fd3f2" stop-opacity="0"/>
          <stop offset="0.5" stop-color="#4fd3f2" stop-opacity="0.9"/>
          <stop offset="1" stop-color="#4fd3f2" stop-opacity="0"/>
        </linearGradient>
      </defs>
      <rect width="330" height="4" fill="url(#beam)"/>
    </svg>
    <div class="server-art" role="img" aria-label="Isometric illustration of blue and violet server racks on a glowing platform with data lines"></div>
    <div class="title-block">
      <p class="kicker">What Are The Biggest<br>Differences Between</p>
      <div class="divider"></div>
      <h1 class="headline">Web 2.0<br>to Web 3.0</h1>
    </div>
  </div>
</body>
</html>
```